LSV AUDITION

I need a post card design (front only) with this on it:
Leap Spin Vibe (this is the main title to be in all caps)
Auditions
Date: Thursday June 30th
6:30-8:30 PM in person
Address: 4170 Wexley BLVD, Oakland CA 94611
video submissions turn in by Sunday July 3rd, 2022 email:LeapSpinVibe22@trovemail.net
Teens and Adults welcomed

SO PLEASE COME UP WITH A DESIGN THATS COLORFUL AND INVITING THX!

```html
<!DOCTYPE html>
<html lang="en">
<head>
<meta charset="utf-8">
<title>LSV Auditions Postcard</title>
<link rel="stylesheet" href="https://fonts.googleapis.com/css2?family=Montserrat:wght@500;600;700;800&family=Oswald:wght@500;600&display=swap">
<style>
  :root {
    --stage: #ffffff;
    --card-black: #05040a;
    --card-navy: #0b0f2a;
    --floor-blue: #1a2356;
    --pink: #f01aa6;
    --magenta: #d21fd0;
    --violet: #6a4fe0;
    --cyan: #19c3f2;
    --white: #ffffff;
    --photo-deep: #1a0626;
    --photo-mid: #4a1760;
    --photo-glow: #8b2a9e;
  }
  html, body {
    margin: 0;
    padding: 0;
    width: 1200px;
    height: 2253px;
    overflow: hidden;
    background: var(--stage);
  }
  .postcard {
    position: absolute;
    left: 50px;
    top: 760px;
    width: 1100px;
    height: 734px;
    overflow: hidden;
    background:
      linear-gradient(180deg, var(--card-black) 0%, var(--card-black) 55%, var(--card-navy) 82%, var(--floor-blue) 100%);
    box-shadow: 0 18px 40px rgba(0,0,0,0.35);
    font-family: "Montserrat", sans-serif;
    color: var(--white);
  }
  .dancer-photo {
    position: absolute;
    left: 560px;
    top: 0;
    width: 540px;
    height: 734px;
    background:
      radial-gradient(ellipse 45% 55% at 62% 45%, var(--photo-glow) 0%, rgba(139,42,158,0.35) 45%, transparent 75%),
      radial-gradient(ellipse 60% 70% at 70% 20%, var(--photo-mid) 0%, transparent 70%),
      linear-gradient(90deg, transparent 0%, var(--photo-deep) 30%, var(--photo-deep) 100%);
  }
  .title {
    position: absolute;
    left: 48px;
    top: 40px;
    margin: 0;
    font-weight: 800;
    font-size: 118px;
    line-height: 92px;
    letter-spacing: -1px;
  }
  .title span { display: block; }
  .title .leap { color: var(--pink); }
  .title .spin {
    background: linear-gradient(90deg, var(--cyan) 0%, var(--violet) 50%, var(--magenta) 85%);
    -webkit-background-clip: text;
    background-clip: text;
    color: transparent;
  }
  .title .vibe { color: var(--cyan); }
  .title-rule {
    position: absolute;
    left: 55px;
    top: 351px;
    width: 430px;
    height: 3px;
    background: linear-gradient(90deg, rgba(255,255,255,0.6), var(--white) 50%, rgba(255,255,255,0.6));
    border-radius: 2px;
  }
  .auditions {
    position: absolute;
    left: 55px;
    top: 368px;
    font-weight: 700;
    font-size: 46px;
    letter-spacing: 0.43em;
    line-height: 1;
  }
  .date-block {
    position: absolute;
    left: 55px;
    top: 448px;
    width: 240px;
  }
  .date-main {
    font-family: "Oswald", sans-serif;
    font-weight: 600;
    font-size: 64px;
    line-height: 64px;
    color: var(--white);
    letter-spacing: -1px;
  }
  .date-main .day-num { color: var(--magenta); }
  .date-main sup {
    font-size: 36px;
    vertical-align: top;
    position: relative;
    top: 2px;
    color: var(--magenta);
  }
  .weekday {
    font-weight: 700;
    font-size: 37px;
    line-height: 40px;
    margin-top: -2px;
  }
  .date-divider {
    position: absolute;
    left: 362px;
    top: 446px;
    width: 2px;
    height: 104px;
    background: var(--white);
  }
  .details {
    position: absolute;
    left: 385px;
    top: 452px;
    font-weight: 600;
  }
  .details .time {
    color: var(--magenta);
    font-size: 25px;
    line-height: 30px;
    margin-bottom: 6px;
  }
  .detail-row {
    display: flex;
    align-items: flex-start;
    gap: 12px;
    font-size: 19px;
    line-height: 22px;
    margin-bottom: 4px;
  }
  .detail-row svg { flex: none; margin-top: 3px; }
  .deadline {
    position: absolute;
    left: 55px;
    top: 598px;
    font-weight: 600;
    font-size: 22px;
    display: flex;
    align-items: center;
    gap: 12px;
  }
  .deadline .highlight {
    background: var(--pink);
    padding: 3px 10px;
    font-weight: 700;
  }
  .welcome {
    position: absolute;
    left: 55px;
    top: 648px;
    font-weight: 700;
    font-size: 37px;
    letter-spacing: 0.02em;
    color: var(--cyan);
  }
</style>
</head>
<body>
  <main class="postcard">
    <div class="dancer-photo" role="img" aria-label="Photo of a young dancer leaping mid-air in a pink top and jeans, wrapped in glowing purple light trails"></div>

    <h1 class="title">
      <span class="leap">LEAP</span>
      <span class="spin">SPIN</span>
      <span class="vibe">VIBE</span>
    </h1>
    <div class="title-rule"></div>
    <div class="auditions">AUDITIONS</div>

    <div class="date-block">
      <div class="date-main"><span class="day-num">30<sup>TH</sup></span> JUNE</div>
      <div class="weekday">THURSDAY</div>
    </div>
    <div class="date-divider"></div>

    <div class="details">
      <div class="time">6:30-8:30 PM in person</div>
      <div class="detail-row">
        <svg width="16" height="20" viewBox="0 0 16 20" aria-hidden="true">
          <path d="M8 1a6 6 0 0 0-6 6c0 4.5 6 10 6 10s6-5.5 6-10a6 6 0 0 0-6-6z" fill="none" stroke="#f01aa6" stroke-width="2.2"/>
          <circle cx="8" cy="7" r="2.2" fill="#f01aa6"/>
          <rect x="1" y="18" width="14" height="2" fill="#f01aa6"/>
        </svg>
        <span>4170 Wexley BLVD, Oakland<br>CA 94611</span>
      </div>
      <div class="detail-row">
        <svg width="20" height="14" viewBox="0 0 20 14" aria-hidden="true">
          <rect x="0" y="0" width="20" height="14" fill="#f01aa6"/>
          <path d="M0 0l10 8 10-8" fill="none" stroke="#05040a" stroke-width="1.6"/>
        </svg>
        <span>LeapSpinVibe22@trovemail.net</span>
      </div>
    </div>

    <div class="deadline">
      <span>Video submissions turn in by</span>
      <span class="highlight">Sunday July 3rd, 2022</span>
    </div>
    <div class="welcome">TEENS AND ADULTS WELCOMED</div>
  </main>
</body>
</html>
```